Ridgeway Hearth Partners Business Card

Looking for a new business card layout. We are a real estate firm w/ a logo, old design attached. Must keep the same elements on there, just need a fresh look and possible some foil accents. Looking for a simpler design w/ more modern style.

Target Market(s)

Real Estate clients

Industry/Entity Type

Real Estate Agent

Contact Information for Business Card

Font styles to use
Sans Serif

Requirements
Must have
• all elements on current biz card
Nice to have
• modern look, simpler than we have!
Should not have
• no serif fonts

```html
<!DOCTYPE html>
<html lang="en">
<head>
<meta charset="utf-8">
<title>Ridgeway Hearth Partners Business Card</title>
<link href="https://fonts.googleapis.com/css2?family=Montserrat:wght@300;400;500;600&display=swap" rel="stylesheet">
<style>
  :root {
    --backdrop: #e6e6e8;
    --card-black: #131313;
    --card-edge: #a9a9ab;
    --silver: #c9c9cb;
    --silver-soft: #9a9a9c;
    --text-light: #e4e4e4;
    --photo-top: #eef0ee;
    --photo-mid: #d8c7a6;
    --photo-low: #3cc3bd;
  }
  * { box-sizing: border-box; margin: 0; padding: 0; }
  html, body { width: 1200px; height: 800px; overflow: hidden; }
  body {
    background: var(--backdrop);
    font-family: "Montserrat", sans-serif;
    position: relative;
  }
  .card {
    position: absolute;
    width: 560px;
    height: 320px;
    background: var(--card-black);
  }
  .card--front {
    left: 320px;
    top: 50px;
    border: 7px solid var(--card-edge);
    display: flex;
  }
  .card--back {
    left: 320px;
    top: 430px;
    display: flex;
    align-items: center;
    justify-content: center;
  }
  .front-info {
    width: 56%;
    padding: 26px 0 0 28px;
    color: var(--text-light);
  }
  .front-photo {
    width: 44%;
    height: 100%;
    background: linear-gradient(180deg, var(--photo-top) 0%, var(--photo-mid) 55%, var(--photo-low) 100%);
  }
  .brand {
    font-weight: 500;
    color: var(--silver);
    text-transform: uppercase;
    line-height: 1.15;
  }
  .brand--small { font-size: 17px; letter-spacing: 2px; }
  .brand--large { font-size: 34px; letter-spacing: 6px; text-align: center; line-height: 1.3; }
  .agent-name {
    margin-top: 20px;
    font-size: 22px;
    font-weight: 300;
    letter-spacing: 1px;
    text-transform: uppercase;
  }
  .agent-title {
    font-size: 10px;
    font-weight: 500;
    letter-spacing: 1px;
    text-transform: uppercase;
    margin-bottom: 14px;
  }
  .contact-list { list-style: none; font-size: 11px; line-height: 1.45; }
  .contact-list li { display: flex; align-items: flex-start; gap: 8px; }
  .contact-list svg { width: 10px; height: 10px; margin-top: 3px; flex: none; fill: var(--text-light); }
  .contact-list .address { margin-bottom: 8px; }
</style>
</head>
<body>
  <section class="card card--front">
    <div class="front-info">
      <p class="brand brand--small">Ridgeway Hearth<br>Partners</p>
      <h1 class="agent-name">Dana Whitley</h1>
      <p class="agent-title">Principal Broker</p>
      <ul class="contact-list">
        <li class="address">
          <svg viewBox="0 0 10 10"><path d="M5 0a3.5 3.5 0 0 0-3.5 3.5C1.5 6 5 10 5 10s3.5-4 3.5-6.5A3.5 3.5 0 0 0 5 0zm0 5a1.4 1.4 0 1 1 0-2.8A1.4 1.4 0 0 1 5 5z"/></svg>
          <span>418 NW Cedar Ave<br>Bend, OR 97701</span>
        </li>
        <li>
          <svg viewBox="0 0 10 10"><path d="M2 0.5l2 2-1 1.2c.6 1.3 1.6 2.3 2.9 2.9l1.2-1 2 2-1.2 1.9C4 9.5.5 6 .1 1.7z"/></svg>
          <span>541.555.0147</span>
        </li>
        <li>
          <svg viewBox="0 0 10 10"><path d="M2.5 0h5v10h-5zM3.3 1v7h3.4V1z"/></svg>
          <span>541.555.0193</span>
        </li>
        <li>
          <svg viewBox="0 0 10 10"><path d="M0 2h10v6H0zm1 1v.3L5 6l4-2.7V3z"/></svg>
          <span>dana@ridgewayhearth.com</span>
        </li>
        <li>
          <svg viewBox="0 0 10 10"><circle cx="5" cy="5" r="4.5"/></svg>
          <span>RidgewayHearth-Homes.com</span>
        </li>
      </ul>
    </div>
    <div class="front-photo" role="img" aria-label="Portrait photo of the broker"></div>
  </section>

  <section class="card card--back">
    <p class="brand brand--large">Ridgeway Hearth<br>Partners</p>
  </section>
</body>
</html>
```